Banner Ad Design Project

I need a banner design. The website is under construction at www.brightmarrow.example

Name: Bright Marrow
Tagline: Steady Sparks for crowded calendars

This is a leadership development and executive coaching site. The past site is live at www.quillstepnow.example. (so you can get a sense of the content)

The audience are (BUSY) executives, senior managers, leaders and top professionals, so the feel needs to be highly professional but also modern and fresh. I want to communicate energy but also solid and trust worthy and not too new agey. The audience are also people with strong social values who want to change things - so not too corporate (Ie suits!)

I would like the design to be floating on a white background, very clean and simple. I am attracted to reds or sunset (burn orange crimson colors.) But totally open to any color ideas.
I am giving an open brief for your ideas.
Here are the dimensions 960px wide, roughly 190px height.

Reason: The weekend might give more time to designers to get involved. Thanks Vina

Hi designers

You may not have seen the additions I gave to this brief.

The banner should not have leader out front photo's. Maybe less corporate than I initially thought. 
Not too corporate (no suits!) Please no chess pieces, jigsaw pieces, cartoon images, cliche leadership images. 
Am am trying for inspiration /inspiring whilst still being professional. Very simple and clean.
Please can the design be floating in a white background so that the web page is borderless - A bit like it is in http://palmoriskel.example/
Thank you

Target Market(s)

Senior managers, executives but people who also want to change the world!

Industry/Entity Type

Construction

Requirements
Should not have
• Should not have leader out front photo's.
Maybe less corporate than I initially thought.
Am am trying for inspiration /inspiring whilst still being professional.
Please no chess pieces, jigsaw pieces, cartoon images, cliche leadership images. Not too corporate (Ie suits!)

Thanks

```html
<!DOCTYPE html>
<html lang="en">
<head>
<meta charset="utf-8">
<title>Bright Marrow – Banner</title>
<link rel="stylesheet" href="https://fonts.googleapis.com/css2?family=Italianno&display=swap">
<style>
  :root {
    --paper: #ffffff;
    --wash: rgba(207, 233, 247, 0.55);
    --wash-fade: rgba(207, 233, 247, 0);
    --ink: #111111;
  }
  html, body {
    margin: 0;
    padding: 0;
    width: 1200px;
    height: 238px;
    overflow: hidden;
    background: var(--paper);
  }
  .banner {
    position: relative;
    width: 1200px;
    height: 238px;
    overflow: hidden;
    background: var(--paper);
  }
  .banner__decoration {
    position: absolute;
    inset: 0;
    background: radial-gradient(ellipse 60% 90% at 72% 45%, var(--wash) 0%, var(--wash-fade) 100%);
  }
  .banner__name {
    position: absolute;
    left: 56px;
    top: 30px;
    margin: 0;
    font-family: "Italianno", cursive;
    font-weight: 400;
    font-size: 94px;
    line-height: 1;
    color: var(--ink);
    letter-spacing: 1px;
    white-space: nowrap;
  }
  .banner__tagline {
    position: absolute;
    left: 412px;
    top: 138px;
    margin: 0;
    font-family: "Italianno", cursive;
    font-weight: 400;
    font-size: 65px;
    line-height: 1;
    color: var(--ink);
    letter-spacing: 0.5px;
    white-space: nowrap;
  }
</style>
</head>
<body>
  <header class="banner">
    <div class="banner__decoration" role="img" aria-label="Soft pale blue translucent bubble decoration floating on white"></div>
    <h1 class="banner__name">Bright Marrow</h1>
    <p class="banner__tagline">Steady Sparks for crowded calendars</p>
  </header>
</body>
</html>
```